Vitamin B12 Liquid Drops Label

hi, i need a label designed for my vitamin b12 drops that i am going to be selling on bazaarly. the label needs to quickly capture the attention of a buyer as he or she is scrolling through the thumbnail search results on bazaarly.net my brand is called zulmo. i already have an example brand logo i will be using, however, i need help designing the rest of the label. attached are some examples of labels i like for other supplements.some of these examples are pink. i do not want pink. please go for a blue/green color scheme. THE DESIGN MUST BE BOLD

Target Market(s)

adults ages 30 - 64

Font styles to use
Sans Serif

Colors
0455a3
cedeed
3176b5
85acd3
cfdeed
9bcb3b
abd037
cadf82
00a990

Requirements
Must have
• - bold design
• - somewhat gender-neutral color scheme because this will be used equally by men and women
• - B12 MUST be very prominent and visible on the label
Should not have
• - it should not be "crunchy" looking

```html
<!DOCTYPE html>
<html lang="en">
<head>
<meta charset="utf-8">
<title>Zulmo Vitamin B12 Label</title>
<link rel="stylesheet" href="https://fonts.googleapis.com/css2?family=Montserrat:wght@500;600;800&display=swap">
<style>
  :root {
    --navy: #323089;
    --green: #9dc93b;
    --green-light: #d3e8a8;
    --paper: #ffffff;
    --backdrop: #e4e4e4;
  }
  html, body {
    margin: 0;
    padding: 0;
    width: 1200px;
    height: 900px;
    overflow: hidden;
    background: var(--backdrop);
  }
  .canvas {
    position: relative;
    width: 1200px;
    height: 900px;
  }
  .label {
    position: absolute;
    left: 60px;
    top: 117px;
    width: 1080px;
    height: 666px;
    display: block;
    box-shadow: 0 6px 24px rgba(0,0,0,0.12);
  }
  .brand-name {
    font-family: "Montserrat", sans-serif;
    font-weight: 800;
    fill: var(--paper);
  }
  .product-kind {
    font-family: "Montserrat", sans-serif;
    font-weight: 600;
    fill: var(--navy);
    letter-spacing: 4px;
  }
  .product-name {
    font-family: "Montserrat", sans-serif;
    font-weight: 600;
    fill: var(--navy);
  }
</style>
</head>
<body>
<main class="canvas">
  <svg class="label" viewBox="0 0 600 370" xmlns="http://www.w3.org/2000/svg" aria-label="Zulmo Vitamin B12 label">
    <defs>
      <linearGradient id="greenFade" x1="0" y1="0" x2="0" y2="1">
        <stop offset="0" stop-color="var(--green-light)"/>
        <stop offset="0.35" stop-color="var(--green)"/>
        <stop offset="1" stop-color="var(--green)"/>
      </linearGradient>
    </defs>

    <rect class="label-ground" x="0" y="0" width="600" height="370" fill="var(--paper)"/>
    <rect class="top-band" x="0" y="0" width="600" height="10" fill="var(--navy)"/>

    <g class="green-field" role="img" aria-label="Decorative layered green wave artwork">
      <rect x="0" y="160" width="600" height="210" fill="url(#greenFade)"/>
    </g>

    <rect class="cross-band" x="0" y="303" width="600" height="20" fill="var(--navy)"/>

    <g class="brand-tag brand-tag-top">
      <rect x="257" y="12" width="100" height="32" fill="var(--navy)"/>
      <text class="brand-name" x="307" y="36" font-size="20" text-anchor="middle">ZULMO</text>
    </g>
    <g class="brand-tag brand-tag-corner">
      <rect x="497" y="20" width="102" height="30" fill="var(--navy)"/>
      <text class="brand-name" x="548" y="43" font-size="20" text-anchor="middle">ZULMO</text>
    </g>

    <text class="product-kind" x="305" y="101" font-size="23" text-anchor="middle">VITAMIN</text>
    <text class="product-name" x="307" y="136" font-size="36" text-anchor="middle">B<tspan font-size="24">12</tspan></text>

    <g class="brand-tag brand-tag-side">
      <rect x="0" y="263" width="102" height="34" fill="var(--navy)"/>
      <text class="brand-name" x="51" y="287" font-size="20" text-anchor="middle">ZULMO</text>
    </g>
    <g class="brand-tag brand-tag-vertical">
      <rect x="179" y="190" width="54" height="178" fill="var(--navy)"/>
      <text class="brand-name" x="0" y="0" font-size="36" text-anchor="middle"
        transform="translate(219 279) rotate(-90)">ZULMO</text>
    </g>
  </svg>
</main>
</body>
</html>
```